Norvale Works" Voyage Check Kit" Instructions Cards

We need to design two 4.25" x 5.5" 2-sided COVID-19 Specimen Collection Instructions Cards. One card is for the collection and testing of RT-PCR Nasal Swab Specimen and the second card is for the collection and testing of a Rapid Antigen Nasal Swab specimen.

Each card will be 4.25" x 5.5", 2-sided, laminated no-edge seal, with 3 color front and 2 color back.

RT-PCR Nasal Swab Collection Kit Instructions:
1. Please see an "example only" of a collection test kit instructions done for PCR Saliva test (see attached 2-sided card).
2. Please see attached PDF of the RT-PCR Nasal Swab Collection instructions. We will need to follow these collection steps instructions but design our own illustrations. With this set of instructions we will have a total of 8 steps.
3. Please see our Nasal Swab Collection device (see attached images), as our nasal swab is a dry collection device.

Rapid Antigen Nasal Swab Collection Kit Instructions:
1. Please see an "example" of a collection test kit instructions done for Rapid Antigen Test (see attached image with instructions). we will need to follow these steps 7 steps and will revise/shorten the copy.
2. We will have a total of 8 steps and will provide detailed copy for each step.

Please email me with any questions you may have: tlinwood@norvaleassays.example

Thank you

Dale

```html
<!DOCTYPE html>
<html lang="en">
<head>
<meta charset="utf-8">
<title>Norvale Works Collection Kit Instruction Cards</title>
<link href="https://fonts.googleapis.com/css2?family=Poppins:wght@300;400;600;700&display=swap" rel="stylesheet">
<style>
  :root {
    --backdrop: #a9a9a9;
    --card: #ffffff;
    --header-bar: #6b6b6b;
    --header-text: #ffffff;
    --ink: #1f1f1f;
    --step-number: #9a9a9a;
    --art-skin: #f3c9a8;
    --art-grey: #e4e4e4;
    --brand-ink: #2a2a2a;
    --brand-blue: #3b4fa8;
  }
  * { box-sizing: border-box; margin: 0; padding: 0; }
  html, body { width: 1200px; height: 738px; overflow: hidden; }
  body {
    background: var(--backdrop);
    font-family: "Poppins", sans-serif;
    color: var(--ink);
    position: relative;
  }
  .card {
    position: absolute;
    top: 61px;
    width: 475px;
    height: 615px;
    background: var(--card);
  }
  .card--pcr { left: 73px; }
  .card--antigen { left: 657px; }
  .card__header {
    position: absolute;
    left: 25px; top: 16px;
    width: 430px; height: 27px;
    background: var(--header-bar);
    color: var(--header-text);
    font-weight: 600;
    font-size: 12.4px;
    line-height: 27px;
    text-align: center;
    letter-spacing: 0.1px;
  }
  .step { position: absolute; left: 0; }
  .step__number {
    position: absolute;
    left: 28px; top: -3px;
    font-weight: 300;
    font-size: 26px;
    line-height: 26px;
    color: var(--step-number);
  }
  .step__text {
    position: absolute;
    left: 53px;
    font-size: 10.4px;
    line-height: 12.1px;
  }
  .art { position: absolute; border-radius: 4px; }
  .art--light { background: linear-gradient(135deg, #f1f1f1, #dcdcdc); }
  .art--hand { background: linear-gradient(135deg, var(--art-skin), #ececec); }
  .note { position: absolute; left: 53px; font-size: 10.4px; line-height: 12.1px; width: 310px; }
  .note__title { font-weight: 600; }
  .brand {
    position: absolute;
    left: 0; width: 100%;
    top: 557px;
    text-align: center;
  }
  .brand__name {
    display: inline-flex;
    align-items: center;
    gap: 8px;
    font-weight: 600;
    font-size: 22px;
    line-height: 26px;
    color: var(--brand-ink);
  }
  .brand__dot {
    width: 20px; height: 20px;
    border-radius: 50%;
    background: var(--brand-blue);
  }
  .brand__legal { font-size: 5px; line-height: 8px; margin-left: 24px; }
</style>
</head>
<body>

<section class="card card--pcr">
  <h2 class="card__header">RT-PCR NASAL SWAB COLLECTION KIT INSTRUCTIONS</h2>

  <div class="step" style="top:68px">
    <span class="step__number">1</span>
    <p class="step__text" style="width:275px">Remove contents where you will open the collection kit. Remove and layout contents of kit. Read instructions before starting specimen collection.</p>
  </div>
  <div class="art art--light" role="img" aria-label="Illustration of an opened collection kit with tube, swab and biohazard bag" style="left:360px;top:53px;width:78px;height:78px"></div>

  <div class="step" style="top:152px">
    <span class="step__number">2</span>
    <p class="step__text" style="width:285px">Remove the swab from the package. Do not touch the soft end with your hands a anything else.</p>
  </div>
  <div class="art art--hand" role="img" aria-label="Illustration of hands peeling open a swab package" style="left:360px;top:143px;width:72px;height:69px"></div>

  <div class="step" style="top:229px">
    <span class="step__number">3</span>
    <p class="step__text" style="width:380px">Insert &amp; slowly rotate the swab, gently pressing against the inside of each nostril at least 4 times for a total of 15 seconds. Get as much nasal discharge as possible on the soft end of the swab.</p>
  </div>

  <div class="step" style="top:299px">
    <span class="step__number">4</span>
    <p class="step__text" style="width:160px;top:3px">Gently Remove the swab</p>
  </div>
  <div class="art art--light" role="img" aria-label="Illustration of a swab being rotated in the nostril" style="left:220px;top:289px;width:100px;height:40px"></div>
  <div class="art art--light" role="img" aria-label="Illustration of a swab being removed from the nostril" style="left:337px;top:289px;width:100px;height:40px"></div>

  <div class="step" style="top:362px">
    <span class="step__number">5</span>
    <p class="step__text" style="width:275px">Place the swab In the sterile tube and snap off the end of the swab at the break line, so that It fits comfortably In the tube. Place the cap on the tube and screw down tightly to prevent leakage.</p>
  </div>
  <div class="art art--hand" role="img" aria-label="Illustration of hands placing the swab into a sterile tube" style="left:341px;top:354px;width:87px;height:63px"></div>

  <div class="step" style="top:436px">
    <span class="step__number">6</span>
    <p class="step__text" style="width:265px">Place the tube containing the swab In the biohazard bag provided and seal the bag. and follow the instructions on the card for shipping to lab for testing.</p>
  </div>
  <div class="art art--light" role="img" aria-label="Illustration of the sealed tube inside a biohazard bag" style="left:345px;top:431px;width:78px;height:66px"></div>

  <div class="note" style="top:500px">
    <p class="note__title">SHIPPING DETAILS:</p>
    <p>Lorem Ipsum is simply dummy text of the printing and typesetting industry. Lorem Ipsum has been the industry's standard dummy text.</p>
  </div>

  <footer class="brand">
    <div class="brand__name"><span class="brand__dot"></span>NORVALE WORKS</div>
    <p class="brand__legal">(c) copyright 2022 Norvale Works laboratories, All Rights Reserved</p>
  </footer>
</section>

<section class="card card--antigen">
  <h2 class="card__header">RAPID ANTIGEN NASAL SWAB COLLECTION KIT INSTRUCTIONS</h2>

  <div class="step" style="top:60px">
    <span class="step__number">1</span>
    <p class="step__text" style="width:275px">Remove the Swab &amp; Test Device from their packaging. Place the Test Device on a horizontal (flat) surface forrunning the test.</p>
  </div>
  <div class="art art--hand" role="img" aria-label="Illustration of hands unwrapping the swab and test device" style="left:339px;top:52px;width:102px;height:64px"></div>

  <div class="step" style="top:116px">
    <span class="step__number">2</span>
    <p class="step__text" style="width:285px">Insert the entire collection tip of the swab provided (usually 1/2 to 3/4 of an inch, or 1 to 1.5 cm) inside the nostril. Firmly sample the nasal wall by rotating the swab in a circular path against the nasal wall at least 4 times. Take approximately 15 seconds to collect the specimen. Be sure to collect any nasal drainage that may be present on the swab.  Repeat in the other nostril using the same swab.</p>
  </div>
  <div class="art art--hand" role="img" aria-label="Illustration of a swab being rotated inside the nostril" style="left:345px;top:131px;width:93px;height:66px"></div>

  <div class="step" style="top:232px">
    <span class="step__number">3</span>
    <p class="step__text" style="width:285px">The Buffer Solution Vial cap is composed of two parts (purple and white). Remove the entire cap. Stir the swab into the Buffer Solution, ensuring that the swab head is fully submerged by tilting the vial.<br>Twist the swab back and forth 20 times in the Buffer Solution. Poll the swab head against the inner wall of the vial to release the liquid from the swab, then discard the swab.</p>
  </div>
  <div class="art art--light" role="img" aria-label="Drawing of the buffer vial cap being removed and the swab stirred" style="left:342px;top:239px;width:93px;height:69px"></div>

  <div class="step" style="top:349px">
    <span class="step__number">4</span>
    <p class="step__text" style="width:275px">Close the entire cap tightly.Immediately perform steps 5-7.</p>
  </div>
  <div class="art art--light" role="img" aria-label="Drawing of the vial with cap closed and top half removed" style="left:339px;top:335px;width:87px;height:81px"></div>

  <div class="step" style="top:391px">
    <span class="step__number">5</span>
    <p class="step__text" style="width:275px">Remove the purple top half of the cap to expose the dropper tip.</p>
  </div>

  <div class="step" style="top:436px">
    <span class="step__number">6</span>
    <p class="step__text" style="width:275px">Hold the vial vertically above the sample well (S). Slowly squeeze and apply 3 drops of the Buffer Solution into the sample well (S) of the Test Device.</p>
  </div>
  <div class="art art--hand" role="img" aria-label="Illustration of drops applied from the vial onto the test device" style="left:348px;top:434px;width:75px;height:60px"></div>

  <div class="note" style="top:493px">
    <p class="note__title">YOUR TEXT HERE</p>
    <p>Lorem Ipsum is simply dummy text of the printing and typesetting industry. Lorem Ipsum has been the industry's standard dummy text.</p>
  </div>

  <footer class="brand">
    <div class="brand__name"><span class="brand__dot"></span>NORVALE WORKS</div>
    <p class="brand__legal">(c) copyright 2022 Norvale Works laboratories, All Rights Reserved</p>
  </footer>
</section>

</body>
</html>
```